Vex9Tax Business Card

Need a new business card for my law firm. The major components for the card will be my logo "Vex9Tax," the photo of me, contact information, and a QR Code for my website vex9tax.com. If you are unable to generate a QR Code, let me know and I'll see if I can make one. For the "Vex9Tax" logo, don't worry about the "Ride The Wave" part, you can leave that out. Here are my and the firm details:
Benedicto R Salazar III
Attorney at Law
Address: 250 Harbor Plaza, Suite 400
Dallas, TX 75201
Office #: 877-482-6173
Cell #: 214-657-3381
Fax #: 469-738-5126
Email: vex@vex9tax.com
Website: vex9tax.com

```html
<!DOCTYPE html>
<html lang="en">
<head>
<meta charset="utf-8">
<title>Vex9Tax Business Card</title>
<link href="https://fonts.googleapis.com/css2?family=Ubuntu:wght@400;500;700&display=swap" rel="stylesheet">
<style>
  :root {
    --page: #ffffff;
    --card-light: #ffffff;
    --card-dark: #000000;
    --ink: #111111;
    --accent: #3ec3f0;
    --reverse: #ffffff;
    --photo-top: #4a4744;
    --photo-bottom: #1c1b1c;
  }
  * { margin: 0; padding: 0; box-sizing: border-box; }
  html, body { width: 1200px; height: 1200px; overflow: hidden; background: var(--page); }
  body { position: relative; font-family: "Ubuntu", sans-serif; color: var(--ink); }

  .card {
    position: absolute;
    left: 165px;
    width: 870px;
    height: 510px;
    box-shadow: 0 2px 8px rgba(0,0,0,0.18);
  }
  .card--front { top: 66px; background: var(--card-light); }
  .card--back { top: 626px; background: var(--card-dark); }

  .brand-name {
    position: absolute;
    font-weight: 700;
    line-height: 1;
    white-space: nowrap;
  }
  .card--front .brand-name {
    left: 57px; top: 64px;
    font-size: 64px;
    letter-spacing: 0.12em;
    color: var(--ink);
  }

  .portrait {
    position: absolute;
    left: 518px; top: 30px;
    width: 295px; height: 259px;
    background: linear-gradient(180deg, var(--photo-top), var(--photo-bottom));
  }

  .attorney { position: absolute; right: 57px; top: 296px; text-align: right; }
  .attorney__name { font-size: 32px; font-weight: 700; color: var(--accent); line-height: 1.15; }
  .attorney__title { font-size: 20px; color: var(--ink); line-height: 1.35; }

  .contact-list { position: absolute; left: 57px; top: 298px; list-style: none; }
  .contact-list li {
    display: flex; align-items: center;
    height: 33.7px;
    font-size: 20px;
  }
  .icon { width: 15px; height: 15px; margin-right: 14px; fill: var(--accent); flex: none; }

  .address { position: absolute; left: 475px; top: 405px; display: flex; }
  .address .icon { margin-top: 4px; margin-right: 11px; }
  .address p { font-size: 20px; line-height: 29px; }

  .card--back .brand-name {
    left: 0; right: 0; top: 205px; text-align: center;
    font-size: 100px;
    letter-spacing: 0.14em;
    text-indent: 0.14em;
    color: var(--reverse);
  }
</style>
</head>
<body>

<section class="card card--front">
  <div class="brand-name">VEX9TAX</div>

  <div class="portrait" role="img" aria-label="Portrait photo of Benedicto R Salazar III"></div>

  <div class="attorney">
    <p class="attorney__name">Benedicto R Salazar III</p>
    <p class="attorney__title">Attorney at Law</p>
  </div>

  <ul class="contact-list">
    <li>
      <svg class="icon" viewBox="0 0 24 24" aria-hidden="true"><path d="M6.6 10.8a15.1 15.1 0 0 0 6.6 6.6l2.2-2.2a1 1 0 0 1 1-.25 11.4 11.4 0 0 0 3.6.57 1 1 0 0 1 1 1V20a1 1 0 0 1-1 1A17 17 0 0 1 3 4a1 1 0 0 1 1-1h3.5a1 1 0 0 1 1 1c0 1.25.2 2.45.57 3.57a1 1 0 0 1-.25 1z"/></svg>
      877-482-6173
    </li>
    <li>
      <svg class="icon" viewBox="0 0 24 24" aria-hidden="true"><path d="M7 1h10a2 2 0 0 1 2 2v18a2 2 0 0 1-2 2H7a2 2 0 0 1-2-2V3a2 2 0 0 1 2-2zm0 3v14h10V4zm5 15.2a1.1 1.1 0 1 0 0 2.2 1.1 1.1 0 0 0 0-2.2z"/></svg>
      214-657-3381
    </li>
    <li>
      <svg class="icon" viewBox="0 0 24 24" aria-hidden="true"><path d="M6 2h12v5H6zM4 8h16a2 2 0 0 1 2 2v7h-4v5H6v-5H2v-7a2 2 0 0 1 2-2zm4 7v5h8v-5z"/></svg>
      469-738-5126
    </li>
    <li>
      <svg class="icon" viewBox="0 0 24 24" aria-hidden="true"><path d="M2 4h20v2l-10 6L2 6zm0 4.3 10 6 10-6V20H2z"/></svg>
      vex@vex9tax.com
    </li>
    <li>
      <svg class="icon" viewBox="0 0 24 24" aria-hidden="true"><path d="M12 1a11 11 0 1 0 0 22 11 11 0 0 0 0-22zm0 2c1 0 2.3 2 2.8 5H9.2C9.7 5 11 3 12 3zM3.5 10h4.6a18 18 0 0 0 0 4H3.5a8.7 8.7 0 0 1 0-4zm6.6 0h3.8a16 16 0 0 1 0 4h-3.8a16 16 0 0 1 0-4zm5.8 0h4.6a8.7 8.7 0 0 1 0 4h-4.6a18 18 0 0 0 0-4zM9.2 16h5.6c-.5 3-1.8 5-2.8 5s-2.3-2-2.8-5z"/></svg>
      vex9tax.com
    </li>
  </ul>

  <div class="address">
    <svg class="icon" viewBox="0 0 24 24" aria-hidden="true"><path d="M12 1a8 8 0 0 0-8 8c0 6 8 14 8 14s8-8 8-14a8 8 0 0 0-8-8zm0 11a3 3 0 1 1 0-6 3 3 0 0 1 0 6z"/></svg>
    <p>250 Harbor Plaza, Suite 400<br>Dallas, TX 75201</p>
  </div>
</section>

<section class="card card--back">
  <div class="brand-name">VEX9TAX</div>
</section>

</body>
</html>
```